Canyon Ridge Early Jump Ball Hoops Classic

This is a flyer to advertise a boys & girls basketball tournament. It will be emailed out to various clubs/organizations in the West in attempt to get them to register for the tournament.
I would like it to have black background with a watermark background of the Salt Lake City city scape. The city scape needs to include the Mountains and downtown buildings of SLC. I would also like a pic of a couple basketball players on the flyer

Colors
85cae6
ffffff

Requirements
Must have
• Black background
• Salt Lake City city scape watermark (showing mountains and downtown buildings)
• Use uploaded info
• Use 1 or 2 uploaded basketball player pics
Nice to have
• Use Carolina blue, black, silver & white for colors

```html
<!DOCTYPE html>
<html lang="en">
<head>
<meta charset="utf-8">
<title>Canyon Ridge Early Jump Ball Hoops Classic</title>
<link href="https://fonts.googleapis.com/css2?family=Lato:wght@400;700;900&family=Roboto+Condensed:wght@400;700&family=Oswald:wght@700&display=swap" rel="stylesheet">
<style>
  :root{
    --carolina:#85cae6;
    --carolina-deep:#5fb3d8;
    --white:#ffffff;
    --night:#070b18;
    --night-blue:#0d1f4d;
    --navy:#0b1f6b;
    --ink:#111827;
    --silver:#b9bec6;
  }
  *{margin:0;padding:0;box-sizing:border-box}
  html,body{width:848px;height:1200px;overflow:hidden;background:#e6e6e6}
  .flyer{position:relative;width:848px;height:1200px;overflow:hidden;
    background:radial-gradient(ellipse at 45% 45%,#1a3a8a 0%,var(--night-blue) 35%,var(--night) 75%);
    font-family:'Lato',sans-serif;color:var(--white)}
  .layer{position:absolute}
  .stars{inset:0;width:848px;height:1200px}
  .action-photo{left:373px;top:262px;width:475px;height:296px;
    background:linear-gradient(180deg,rgba(120,130,160,.35),rgba(60,70,100,.15));}
  .skyline-photo{left:0;top:760px;width:848px;height:360px;
    background:linear-gradient(180deg,rgba(40,50,70,0) 0%,rgba(70,80,100,.45) 35%,rgba(30,35,45,.8) 100%);}
  .player-photo{left:17px;top:148px;width:357px;height:667px;border-radius:40% 40% 30% 30%/20% 20% 15% 15%;
    background:radial-gradient(ellipse at 50% 45%,var(--carolina) 0%,#5aa8cc 45%,rgba(90,168,204,0) 72%);}
  .header{left:0;top:0;width:848px;height:270px}
  .brand{left:300px;top:40px;width:260px;text-align:center;color:var(--navy)}
  .brand-name{font-weight:900;font-size:26px;line-height:1.08;text-transform:uppercase}
  .brand-tag{margin-top:10px;font-weight:900;font-size:15px;letter-spacing:.5px;text-transform:uppercase}
  .price{left:593px;top:39px;width:200px;height:200px;border-radius:50%;background:var(--white);
    border:9px solid var(--carolina);display:flex;flex-direction:column;align-items:center;justify-content:center;color:var(--ink)}
  .price-amount{font-family:'Oswald',sans-serif;font-size:60px;line-height:1;font-weight:700}
  .price-unit{font-weight:700;font-size:26px;color:var(--navy);margin-top:4px}
  .event-meta{left:380px;top:385px;width:420px;text-align:center;font-weight:700;font-size:37px;line-height:49px}
  .event-meta span{color:var(--carolina)}
  .qualifier-card{left:285px;top:561px;width:543px;height:232px;border-radius:12px;
    background:linear-gradient(180deg,#f4f5f7,#aeb3bb 50%,#f4f5f7);padding:8px}
  .qualifier-inner{width:100%;height:100%;background:var(--white);border-radius:8px;border:1px solid var(--silver);
    text-align:center;padding-top:34px}
  .qualifier-kicker{font-family:'Lato',sans-serif;font-weight:700;font-size:30px;letter-spacing:1px;color:var(--ink)}
  .qualifier-title{font-family:'Roboto Condensed',sans-serif;font-weight:700;font-size:58px;line-height:1;color:var(--navy);margin-top:2px}
  .qualifier-pill{display:inline-block;margin-top:12px;padding:4px 22px;border:2px solid var(--navy);border-radius:22px;
    font-family:'Roboto Condensed',sans-serif;font-size:31px;color:var(--navy)}
  .venue{left:285px;top:808px;width:543px;text-align:center}
  .venue-head{font-weight:700;font-size:28px;color:var(--carolina)}
  .venue-address{font-weight:700;font-size:18px;margin-top:4px}
  .venue-email{font-weight:700;font-size:16px;margin-top:6px}
  .venue-call{font-weight:700;font-size:22px;margin-top:6px}
  .rules{left:26px;top:976px;width:450px;list-style:none;font-size:10.5px;line-height:12.5px}
  .rules li{position:relative;padding-left:12px;margin-bottom:1px}
  .rules li::before{content:"";position:absolute;left:0;top:4px;width:5px;height:5px;border-radius:50%;background:var(--carolina)}
  .qualifier-notes{left:549px;top:975px;width:255px;font-size:13.5px;line-height:17px}
  .qualifier-notes h3{font-size:15px;font-weight:700;color:var(--carolina);margin-bottom:4px}
  .qualifier-notes p{margin-bottom:6px}
  .footer{left:0;top:1080px;width:848px;height:120px}
  .web{right:44px;top:1145px;font-size:20px;letter-spacing:6px;font-weight:700;color:var(--ink)}
</style>
</head>
<body>
<main class="flyer">
  <svg class="layer stars" viewBox="0 0 848 1200" aria-hidden="true">
    <g fill="#ffffff" opacity=".55">
      <circle cx="40" cy="300" r="1.2"/><circle cx="120" cy="420" r="1"/><circle cx="210" cy="330" r="1.4"/>
      <circle cx="60" cy="560" r="1"/><circle cx="300" cy="480" r="1.2"/><circle cx="420" cy="300" r="1"/>
      <circle cx="520" cy="600" r="1.3"/><circle cx="640" cy="520" r="1"/><circle cx="760" cy="330" r="1.2"/>
      <circle cx="810" cy="600" r="1"/><circle cx="150" cy="680" r="1.3"/><circle cx="350" cy="650" r="1"/>
      <circle cx="90" cy="760" r="1.2"/><circle cx="700" cy="700" r="1"/><circle cx="250" cy="560" r="1"/>
      <circle cx="470" cy="400" r="1.4"/><circle cx="20" cy="450" r="1"/><circle cx="180" cy="250" r="1"/>
    </g>
  </svg>

  <div class="layer action-photo" role="img" aria-label="Faded photo of youth basketball players and a referee on court"></div>
  <div class="layer skyline-photo" role="img" aria-label="Faint Salt Lake City skyline with mountains and downtown buildings"></div>

  <svg class="layer header" viewBox="0 0 848 270" aria-hidden="true">
    <polygon points="0,100 429,232 848,100 848,132 429,262 0,132" fill="var(--carolina)"/>
    <polygon points="0,0 848,0 848,100 429,232 0,100" fill="var(--white)"/>
  </svg>

  <div class="layer brand">
    <div class="brand-name">Canyon Ridge Early Jump Ball Hoops Classic</div>
    <div class="brand-tag">YHF Super Regional</div>
  </div>

  <div class="layer price">
    <div class="price-amount">$425</div>
    <div class="price-unit">per team</div>
  </div>

  <div class="layer player-photo" role="img" aria-label="Girl in light blue uniform dribbling a basketball"></div>

  <div class="layer event-meta">
    <div>Date: <span>MAY 5-6</span></div>
    <div>Division: <span>Div I &amp; Div II</span></div>
  </div>

  <section class="layer qualifier-card">
    <div class="qualifier-inner">
      <div class="qualifier-kicker">YHF SUPER REGIONAL</div>
      <div class="qualifier-title">National Qualifier</div>
      <div class="qualifier-pill">Boys &amp; Girls 2nd - 8th</div>
    </div>
  </section>

  <section class="layer venue">
    <div class="venue-head">ALL UNDER 1 ROOF</div>
    <div class="venue-address">Summit Court Events Hall 2180 W. 900 S. Salt Lake City, UT</div>
    <div class="venue-email">Email: events@canyonridgehoops.com</div>
    <div class="venue-call">CALL US: (801) 555-0142</div>
  </section>

  <ul class="layer rules">
    <li>This event is licensed by the Youth Hoops Federation of the U.S., Inc.</li>
    <li>All participants must have a current YHF membership.</li>
    <li>YHF membership may not be included as part of the entry fee to the event.</li>
    <li>YHF membership must be obtained before the competition begins except where the event operator has a laptop available with an internet connection.</li>
    <li>Participants are encouraged to visit the YHF web site www.yhfhoops.org to obtain their membership.</li>
  </ul>

  <section class="layer qualifier-notes">
    <h3>NATIONAL QUALIFYER:</h3>
    <p>4 game guarantee</p>
    <p>West Coast Super Regional Event. Already confirmed teams from UT, NV, OR, ID, CO, WY, CA, WA, MT</p>
  </section>

  <svg class="layer footer" viewBox="0 0 848 120" aria-hidden="true">
    <polygon points="0,88 848,6 848,120 0,120" fill="var(--white)"/>
    <polygon points="0,96 848,16 848,120 0,120" fill="var(--carolina)"/>
  </svg>
  <div class="layer web">www.canyonridgehoops.com</div>
</main>
</body>
</html>
```